Improved Business Card, Government Contracting

We are looking to update the design of our business cards. We would like to create a template that can be used for future employees and easy to update.

Halvorsen Advisory Partners, LLC is a Service Disabled Veteran Owned Small Business with headquarters located in Corwin Falls, OR. Our current website is www.hapteam.com. We have contracts in KS and VA with expansion opportunities in various other states. Our primary line of work is within government contracting and providing consulting services to various organizations within the Bureau of Frontier Works. We would like to project a professional image of our company that is consistent with the industry. Provided are previous versions of our business card template that shows our logo as well. We would like to make sure the information on the cards are easily noticeable .

Target Market(s)

Government Officials
Fellow Small Business Contractors
Large Business Contractors (ex. TRUX, Keswell Barnaby, Pryde Okonjo Whitcombe)

Industry/Entity Type

Business

Contact Information for Business Card

Dale Fenwick
Office Manager
Halvorsen Advisory Partners
Ph: 913.555.0172
Email: d.fenwick@hapteam.us
www.hapteam.com

Requirements
Must have
• The business mailing address is:
• 31842 204th Lane
• Corwin Falls, OR 66099
Nice to have
• Embossed lettering

```html
<!DOCTYPE html>
<html lang="en">
<head>
<meta charset="utf-8">
<title>Halvorsen Advisory Partners – Business Card</title>
<link rel="stylesheet" href="https://fonts.googleapis.com/css2?family=Source+Sans+3:wght@400;600&display=swap">
<style>
  :root {
    --bg: #3a3a3a;
    --card-white: #fbfbfb;
    --brand-blue: #3d58a3;
    --brand-yellow: #f7f06a;
    --text-grey: #444444;
    --rule-grey: #8a8a8a;
    --band-grey: #b8b9bb;
  }
  * { margin: 0; padding: 0; box-sizing: border-box; }
  html, body {
    width: 1200px; height: 750px; overflow: hidden;
    background: var(--bg);
    font-family: "Source Sans 3", sans-serif;
  }
  .canvas { position: relative; width: 1200px; height: 750px; }
  .card {
    position: absolute; top: 218px;
    width: 492px; height: 281px;
    overflow: hidden;
  }
  .card--front { left: 92px; background: var(--card-white); }
  .card--back { left: 620px; background: var(--brand-blue); }

  .company-mark {
    position: absolute; left: 260px; top: 52px; width: 200px;
    text-align: center;
    color: var(--brand-blue);
    font-weight: 600; font-size: 20px; line-height: 23px;
  }
  .name-marker { position: absolute; left: 0; top: 135px; }
  .identity { position: absolute; left: 34px; top: 128px; color: var(--text-grey); }
  .identity__name { color: var(--brand-blue); font-weight: 600; font-size: 16px; line-height: 20px; }
  .identity__line { font-size: 11.5px; line-height: 14px; }
  .divider {
    position: absolute; left: 34px; top: 182px; width: 424px; height: 1.5px;
    background: var(--rule-grey);
  }
  .address {
    position: absolute; left: 34px; top: 219px;
    color: var(--text-grey); font-size: 11.5px; line-height: 16px;
    font-style: normal;
  }
  .contacts {
    position: absolute; right: 36px; top: 202px;
    list-style: none; color: var(--text-grey); font-size: 11.5px;
  }
  .contacts__item {
    display: flex; justify-content: flex-end; align-items: center;
    gap: 7px; height: 16px;
  }
  .contacts__item svg { width: 11px; height: 11px; fill: var(--brand-blue); }
  .footer-band {
    position: absolute; left: 0; bottom: 0; width: 100%; height: 20px;
    background: var(--band-grey);
  }
  .footer-band svg { position: absolute; left: 302px; top: 0; }
  .web {
    position: absolute; left: 302px; bottom: 0; width: 156px; height: 20px;
    line-height: 20px; text-align: center;
    color: var(--brand-yellow); font-size: 11.5px;
  }
  .back-name {
    position: absolute; inset: 0;
    display: flex; flex-direction: column; align-items: center; justify-content: center;
    color: var(--brand-yellow); font-size: 36px; font-weight: 400;
    line-height: 40px; letter-spacing: 0.5px; text-align: center;
  }
</style>
</head>
<body>
<main class="canvas">
  <section class="card card--front" aria-label="Card front">
    <div class="company-mark">Halvorsen Advisory<br>Partners</div>

    <svg class="name-marker" width="19" height="39" viewBox="0 0 19 39" aria-hidden="true">
      <polygon points="0,0 19,19.5 0,39" fill="var(--brand-blue)"/>
    </svg>
    <div class="identity">
      <p class="identity__name">Dale Fenwick</p>
      <p class="identity__line">Halvorsen Advisory Partners, LLC</p>
      <p class="identity__line">Office Manager</p>
    </div>
    <div class="divider"></div>

    <address class="address">
      31842 204th Lane<br>Corwin Falls, OR 66099
    </address>

    <ul class="contacts">
      <li class="contacts__item">555.555.0148
        <svg viewBox="0 0 12 12" aria-label="Phone"><path d="M1 4.5C1 2.5 3 2 6 2s5 .5 5 2.5v1H8.5V4.3H3.5v1.2H1z"/><rect x="2.5" y="6" width="7" height="4.5" rx="1"/></svg>
      </li>
      <li class="contacts__item">555.555.0193
        <svg viewBox="0 0 12 12" aria-label="Fax"><rect x="3" y="1" width="6" height="3"/><rect x="1" y="4.5" width="10" height="4.5" rx="1"/><rect x="3" y="7.5" width="6" height="3.5" fill="#fff" stroke="var(--brand-blue)" stroke-width="1"/></svg>
      </li>
      <li class="contacts__item">d.fenwick@hapteam.us
        <svg viewBox="0 0 12 12" aria-label="Email"><rect x="0.5" y="2" width="11" height="8"/><polyline points="1,2.5 6,7 11,2.5" fill="none" stroke="#fff" stroke-width="1"/></svg>
      </li>
    </ul>

    <div class="footer-band">
      <svg width="156" height="20" viewBox="0 0 156 20" aria-hidden="true">
        <polygon points="10,0 144,0 156,20 0,20" fill="var(--brand-blue)"/>
      </svg>
    </div>
    <div class="web">www.hapteam.com</div>
  </section>

  <section class="card card--back" aria-label="Card back">
    <div class="back-name"><span>Halvorsen</span><span>Advisory Partners</span></div>
  </section>
</main>
</body>
</html>
```